Swing Dance Themed Cleaning Company Website

We need a website designed for a cleaning company based in Portland, Oregon called Foxtrot Lane. We clean homes and commercial buildings, inside and out.

needs to be vintage and like the velvet moonbeam. Speakeasy 1920s feel.
needs to be classy.

Check out foxtrotlane.com We are not happy with the site currently.

please look at house scout site for more content https://www.housescoutly.com/rated.FoxtrotLaneCleaning.41827463.html

Check out my videos on my ClipTube channel Foxtrot Lane

Target Market(s)

middle class and home owner

Industry/Entity Type

Cleaning Service

Number of Pages Required

3 page

Font styles to use
Other font styles liked:
• jazzrag

Colors

Designer to choose colors to be used in the design.

Requirements
Must have
• must be good on pc and mobile

```html
<!DOCTYPE html>
<html lang="en">
<head>
<meta charset="utf-8">
<title>Foxtrot Lane — Cleaning Services in Portland</title>
<link href="https://fonts.googleapis.com/css2?family=Poiret+One&family=Oswald:wght@400;600&family=Open+Sans:ital,wght@0,400;0,700;1,400&display=swap" rel="stylesheet">
<style>
:root{
  --gold:#f7e51c;
  --gold-deep:#d9c416;
  --ink:#0b0b0b;
  --ink-soft:#161514;
  --paper:#e9dcbc;
  --paper-dark:#d6c59c;
  --frame:#a98a4e;
  --text-light:#e8e2d2;
  --text-muted:#a59f90;
  --text-dark:#2a2419;
}
*{box-sizing:border-box;margin:0;padding:0}
html,body{width:1200px;height:3704px;overflow:hidden}
body{position:relative;background:var(--ink);font-family:"Open Sans",sans-serif;color:var(--text-light)}
section,header,footer{position:absolute;left:0;width:1200px}
.display{font-family:"Poiret One",cursive;font-weight:400}
.caps{font-family:"Oswald",sans-serif;text-transform:uppercase;letter-spacing:.5px}
.btn{display:inline-block;background:var(--gold);color:var(--ink);font-family:"Oswald",sans-serif;font-weight:600;font-size:14px;text-transform:uppercase;padding:10px 26px;border-radius:6px;letter-spacing:.5px}
.paper{background:radial-gradient(ellipse at center,#f1e6c9 0%,var(--paper) 55%,var(--paper-dark) 100%)}
.photo{border:5px solid var(--frame);position:absolute}
.section-title{position:absolute;left:0;width:1200px;text-align:center;font-size:38px;letter-spacing:1px}
.section-title span{position:relative;padding:0 28px}
.rule{position:absolute;top:50%;width:150px;height:2px;background:currentColor}
.rule.l{right:100%}.rule.r{left:100%}
.arrow{position:absolute;font-size:34px;color:var(--text-light);font-family:"Oswald",sans-serif}

/* header */
.site-header{top:0;height:91px;background:var(--ink)}
.logo{position:absolute;left:170px;top:12px;display:flex;align-items:center;gap:8px}
.logo-mark{width:24px;height:24px;background:var(--gold)}
.logo-name{font-family:"Oswald",sans-serif;font-weight:600;font-size:24px;color:var(--gold);line-height:1;text-transform:uppercase}
.logo-tag{position:absolute;left:170px;top:44px;font-size:8px;color:var(--gold);font-family:"Oswald",sans-serif;letter-spacing:.6px}
.topbar{position:absolute;left:425px;top:4px;width:615px;height:28px;background:var(--gold);border-radius:0 0 14px 14px;display:flex;align-items:center;gap:26px;padding:0 22px;font-size:10px;color:var(--ink)}
.topbar b{font-family:"Oswald",sans-serif}
.topbar .search{margin-left:auto;width:150px;height:18px;background:#fff8b0;border-radius:3px;padding:2px 8px;color:#8a7d20}
.main-nav{position:absolute;top:56px;left:390px;width:670px;display:flex;justify-content:space-between;font-size:12px}
.main-nav a{color:var(--text-light);text-decoration:none}
.main-nav a.current{color:var(--gold);border-bottom:2px solid var(--gold);padding-bottom:4px}

/* hero */
.hero{top:91px;height:514px;background:linear-gradient(120deg,#d8d2c8 0%,#b9ad98 35%,#6f7760 60%,#c9c2b4 100%)}
.hero-copy{position:absolute;top:215px;width:1200px;text-align:center}
.hero-copy h1{font-family:"Poiret One",cursive;font-weight:400;font-size:38px;color:#fff;line-height:1.2;letter-spacing:1px;text-transform:uppercase;text-shadow:0 2px 6px rgba(0,0,0,.6)}
.hero-copy .btn{margin-top:18px}
.dots{position:absolute;bottom:18px;width:1200px;display:flex;justify-content:center;gap:8px}
.dots i{width:8px;height:8px;border-radius:50%;background:#fff;opacity:.6}
.dots i.on{opacity:1;background:var(--gold)}

/* about */
.about{top:605px;height:482px}
.about-video{left:200px;top:52px;width:355px;height:240px;background:linear-gradient(160deg,#5a3f28,#2a1c12 60%,#7a5a36)}
.play{position:absolute;left:148px;top:92px;width:48px;height:48px;border-radius:50%;background:var(--gold)}
.play::after{content:"";position:absolute;left:19px;top:14px;border-left:14px solid var(--ink);border-top:10px solid transparent;border-bottom:10px solid transparent}
.about-text{position:absolute;left:598px;top:60px;width:400px;color:var(--text-dark)}
.about-text h2{font-size:30px;color:var(--ink)}
.about-text h3{font-size:12px;font-weight:700;margin:12px 0 14px;font-family:"Open Sans",sans-serif}
.about-text p{font-size:10px;line-height:1.6;margin-bottom:6px;color:#5a4f3a}
.about-text .btn{margin-top:10px;font-size:11px;padding:7px 18px}
.feature-row{position:absolute;top:300px;left:180px;width:860px;display:flex;justify-content:space-between}
.feature{width:200px;text-align:center;color:var(--ink);font-size:11px;font-weight:700}
.badge-icon{width:76px;height:76px;border-radius:50%;background:var(--ink);margin:0 auto 12px;display:flex;align-items:center;justify-content:center}

/* services */
.services{top:1087px;height:642px;background:var(--ink)}
.services .section-title{top:38px;color:var(--text-light)}
.tabs{position:absolute;top:108px;width:1200px;display:flex;justify-content:center;gap:12px}
.tab{font-family:"Oswald",sans-serif;font-size:12px;padding:7px 22px;border-radius:6px;border:1px solid var(--text-light)}
.tab.active{background:var(--gold);color:var(--ink);border-color:var(--gold)}
.service-card{position:absolute;top:168px;width:245px;text-align:center}
.service-card .photo{position:relative;width:245px;height:160px}
.service-card h4{font-size:22px;color:var(--gold);margin:14px 0 10px}
.service-card li{list-style:none;font-size:11px;line-height:2.1;font-family:"Oswald",sans-serif;text-transform:uppercase;color:var(--text-light)}
.pricing{position:absolute;top:514px;width:1200px;text-align:center;font-size:11px;font-family:"Oswald",sans-serif}
.pricing b{color:var(--gold)}
.services .cta{position:absolute;top:546px;width:1200px;text-align:center}

/* why */
.why{top:1729px;height:358px}
.why .section-title{top:48px;color:var(--ink)}
.why-figure{position:absolute;left:505px;top:112px;width:190px;height:225px;background:linear-gradient(180deg,#d9cca8,#8a7d62 50%,#d9cca8);border-radius:6px}
.why-item{position:absolute;display:flex;align-items:center;gap:16px;font-size:11px;font-weight:700;color:var(--ink);text-transform:uppercase;line-height:1.5;width:330px}
.why-item.left{flex-direction:row-reverse;text-align:right}
.why-item .badge-icon{width:54px;height:54px;margin:0;flex:none}

/* area */
.area{top:2087px;height:346px;background:var(--ink)}
.area-map{position:absolute;left:210px;top:50px;width:290px;height:258px;background:linear-gradient(135deg,#8c7350,#5e4a30);border-radius:6px}
.area-title{position:absolute;left:555px;top:88px;font-size:34px}
.area-search{position:absolute;left:555px;top:145px;width:280px;height:34px;background:#fff;border-radius:6px;border:3px solid var(--gold);font-size:10px;color:#999;padding:8px 10px}
.area-list{position:absolute;left:560px;top:200px;display:grid;grid-template-columns:110px 110px;row-gap:14px;font-size:10px;text-transform:uppercase;font-family:"Oswald",sans-serif}
.area-list li{list-style:none}
.area-list li::before{content:"• ";color:var(--gold)}

/* blog */
.blog{top:2433px;height:457px;background:linear-gradient(180deg,#1b1a18,#0e0d0c 50%,#1d1c1a)}
.blog .section-title{top:32px}
.post{position:absolute;top:118px;width:240px}
.post .photo{position:relative;width:240px;height:160px;border-color:#d8d0bf}
.date{position:absolute;left:8px;top:0;background:var(--gold);color:var(--ink);width:36px;text-align:center;font-family:"Oswald",sans-serif;font-size:13px;line-height:1.1;padding:3px 0}
.date small{display:block;font-size:7px}
.post h5{font-family:"Poiret One",cursive;color:var(--gold);font-size:15px;margin:12px 0 6px;line-height:1.2;text-transform:uppercase}
.post p{font-size:10px;line-height:1.6;color:var(--text-muted)}
.blog .cta{position:absolute;top:400px;width:1200px;text-align:center}

/* testimonials */
.testimonials{top:2890px;height:272px;background:var(--ink)}
.testimonials .section-title{top:30px}
.quote{position:absolute;top:110px;width:390px;display:flex;gap:16px}
.avatar{width:80px;height:80px;border-radius:50%;background:linear-gradient(135deg,#b8aa98,#6e6458);flex:none}
.quote p{font-size:10px;line-height:1.6;font-style:italic;color:var(--text-muted)}
.quote .name{margin-top:8px;font-family:"Poiret One",cursive;color:var(--gold);font-size:13px}
.quote .name i{color:var(--text-muted);font-style:normal;font-size:10px;margin-left:6px}

/* badges */
.badges{top:3162px;height:135px;display:flex;justify-content:center;align-items:center;gap:80px}
.cert{width:110px;height:86px;background:#8f8a80}
.cert.round{border-radius:50%;width:96px;height:96px}
.cert.shield{clip-path:polygon(0 0,100% 0,100% 70%,50% 100%,0 70%);width:90px}

/* contact */
.contact{top:3297px;height:371px;background:linear-gradient(180deg,#191816,#0f0e0d)}
.contact .section-title{top:40px}
.contact-nav{position:absolute;top:108px;left:270px;width:660px;display:flex;justify-content:space-between;font-size:11px}
.contact-nav .current{color:var(--gold)}
.contact-info{position:absolute;left:270px;top:160px;font-size:10px;line-height:1.5}
.contact-info li{list-style:none;display:flex;gap:12px;margin-bottom:18px;align-items:flex-start}
.dot-icon{width:22px;height:22px;border-radius:50%;background:var(--gold);flex:none;display:flex;align-items:center;justify-content:center}
.contact-form{position:absolute;left:560px;top:150px;width:380px;display:grid;grid-template-columns:1fr 1fr;gap:8px}
.field{background:#2a2927;height:28px;font-size:9px;padding:8px;color:#8a857c}
.field.wide{grid-column:span 2;height:62px}
.contact-form .btn{grid-column:1;width:104px;padding:7px 12px;font-size:11px;margin-top:6px}

/* footer */
.site-footer{top:3668px;height:36px;background:var(--gold);color:var(--ink);font-size:10px;display:flex;align-items:center;justify-content:space-between;padding:0 170px}
.social{display:flex;gap:8px}
.social i{width:20px;height:20px;border-radius:50%;border:1.5px solid var(--ink)}
</style>
</head>
<body>

<header class="site-header">
  <div class="logo"><span class="logo-mark"></span><span class="logo-name">Foxtrot Lane</span></div>
  <div class="logo-tag">BEST CLEANING CLUB IN PORTLAND</div>
  <div class="topbar">
    <b>EMERGENCY SERVICE</b>
    <span>&#9742; 503-555-0148</span>
    <span>&#9993; hello@foxtrotlane.com</span>
    <span class="search">Search</span>
  </div>
  <nav class="main-nav caps">
    <a class="current">Home</a><a>About Us</a><a>Our Services</a><a>Blog</a><a>Contact Us</a>
  </nav>
</header>

<section class="hero" role="img" aria-label="Photo of two cleaners in green uniforms wiping a table and mopping a bright living room">
  <div class="hero-copy">
    <h1>Looking for home and commercial buildings<br>cleaning services in Portland?</h1>
    <span class="btn">Contact Us Today!</span>
  </div>
  <div class="dots"><i></i><i class="on"></i><i></i></div>
</section>

<section class="about paper">
  <div class="photo about-video" role="img" aria-label="Video still with vintage Portland title lettering"><span class="play"></span></div>
  <div class="about-text">
    <h2 class="display">ABOUT US</h2>
    <h3>MAKING THE GREATER PORTLAND AREA CLEAN, ONE BUILDING AT A TIME</h3>
    <p>Foxtrot Lane is a family owned professional cleaning business. We provide our years of cleaning experience to homes and businesses in and around Portland, Oregon. If you need something cleaned, have it cleaned the right way — contact us. Any doubts you have will be wiped away by our fantastic service.</p>
    <p>Our most commonly performed services are listed here, but if you have a special project, let us know. We can clean just about anything!</p>
    <span class="btn">Read More</span>
  </div>
  <div class="feature-row">
    <div class="feature"><div class="badge-icon"><svg width="34" height="34" viewBox="0 0 34 34" fill="none" stroke="#f7e51c" stroke-width="3"><path d="M17 4v18M10 30l7-8 7 8"/></svg></div>CLEANING &amp; MAID SERVICES</div>
    <div class="feature"><div class="badge-icon"><svg width="34" height="34" viewBox="0 0 34 34" fill="#f7e51c"><circle cx="17" cy="11" r="6"/><path d="M6 31c0-7 5-11 11-11s11 4 11 11z"/></svg></div>JANITORIAL</div>
    <div class="feature"><div class="badge-icon"><svg width="34" height="34" viewBox="0 0 34 34" fill="#f7e51c"><rect x="5" y="20" width="24" height="8" rx="2"/><rect x="15" y="4" width="4" height="17"/></svg></div>CARPET CLEANING</div>
    <div class="feature"><div class="badge-icon"><svg width="34" height="34" viewBox="0 0 34 34" fill="none" stroke="#f7e51c" stroke-width="3"><rect x="6" y="6" width="22" height="22"/><path d="M17 6v22M6 17h22"/></svg></div>WINDOW WASHING</div>
  </div>
</section>

<section class="services">
  <h2 class="section-title display"><span><i class="rule l"></i>OUR SERVICES<i class="rule r"></i></span></h2>
  <div class="tabs"><span class="tab active">RESIDENTIAL SERVICES</span><span class="tab">COMMERCIAL SERVICES</span></div>
  <span class="arrow" style="left:150px;top:240px">&#8249;</span>
  <span class="arrow" style="left:1035px;top:240px">&#8250;</span>
  <div class="service-card" style="left:210px">
    <div class="photo" role="img" aria-label="Gloved hand wiping a stovetop with a pink cloth" style="background:linear-gradient(135deg,#b7b0a4,#3b3a38 60%,#c66a9a)"></div>
    <h4 class="display">GENERAL HOUSE KEEPING</h4>
    <ul><li>Floor to ceiling dusting</li><li>Cobweb removal</li><li>Kitchen cleaning</li><li>Bathroom cleaning</li><li>Sweep, mop and vacuum floors</li></ul>
  </div>
  <div class="service-card" style="left:478px">
    <div class="photo" role="img" aria-label="Cleaning crew in uniforms holding supplies" style="background:linear-gradient(135deg,#e6e3dc,#4f6a3c 55%,#e2cf6a)"></div>
    <h4 class="display">MOVE OUTS DETAIL</h4>
    <ul><li>All general house keeping</li><li>Make your house "move in" ready</li><li>Refrigerator and oven cleaning</li><li>Window washing</li><li>Carpet cleaning</li></ul>
  </div>
  <div class="service-card" style="left:745px">
    <div class="photo" role="img" aria-label="Worker pressure washing a garden patio" style="background:linear-gradient(135deg,#9aa08a,#5c6a4c 50%,#c8c4b4)"></div>
    <h4 class="display">EXTERIOR SERVICES</h4>
    <ul><li>Leaf blowing</li><li>Pressure washing</li><li>Window washing</li><li>Exterior house detail</li><li>Gutter cleaning</li></ul>
  </div>
  <p class="pricing"><b>PRICING:</b> $80 PER 1,000 SQUARE FEET FOR USUAL HOUSEKEEPING SERVICES. CALL FOR AN ESTIMATE FOR OTHER SERVICES.</p>
  <div class="cta"><span class="btn">Get an estimate call 503-555-0148</span></div>
</section>

<section class="why paper">
  <h2 class="section-title display"><span><i class="rule l"></i>WHY CHOOSE US<i class="rule r"></i></span></h2>
  <div class="why-figure" role="img" aria-label="Vintage line drawing of a dapper dancer sweeping with a mop"></div>
  <div class="why-item left" style="left:140px;top:135px"><div class="badge-icon"><svg width="24" height="24" viewBox="0 0 24 24" fill="none" stroke="#f7e51c" stroke-width="2.5"><circle cx="12" cy="12" r="9"/><path d="M12 7v5l4 2"/></svg></div><span>We provide efficient planning systems to save you money.</span></div>
  <div class="why-item left" style="left:140px;top:225px"><div class="badge-icon"><svg width="24" height="24" viewBox="0 0 24 24" fill="#f7e51c"><circle cx="12" cy="8" r="4"/><path d="M4 21c0-5 4-8 8-8s8 3 8 8z"/></svg></div><span>We provide a dedicated team to deliver the best service.</span></div>
  <div class="why-item" style="left:730px;top:135px"><div class="badge-icon"><svg width="24" height="24" viewBox="0 0 24 24" fill="none" stroke="#f7e51c" stroke-width="3"><path d="M5 12l5 5 9-10"/></svg></div><span>We provide outstanding service on time every time.</span></div>
  <div class="why-item" style="left:730px;top:225px"><div class="badge-icon"><svg width="24" height="24" viewBox="0 0 24 24" fill="#f7e51c"><path d="M12 3l2.6 6 6.4.5-4.9 4.2 1.5 6.3L12 16.6 6.4 20l1.5-6.3L3 9.5 9.4 9z"/></svg></div><span>We provide cost effective and innovative cleaning solutions.</span></div>
</section>

<section class="area">
  <div class="area-map" role="img" aria-label="Map of the Portland metro service area"></div>
  <h2 class="area-title display">SERVICE AREA WE SERVE</h2>
  <div class="area-search">Search</div>
  <ul class="area-list"><li>Portland</li><li>Tualatin</li><li>Beaverton</li><li>Boring</li><li>Lake Oswego</li></ul>
</section>

<section class="blog">
  <h2 class="section-title display"><span><i class="rule l"></i>LATEST BLOG<i class="rule r"></i></span></h2>
  <span class="arrow" style="left:160px;top:190px">&#8249;</span>
  <span class="arrow" style="left:1025px;top:190px">&#8250;</span>
  <article class="post" style="left:210px">
    <div class="photo" role="img" aria-label="Guitarist performing on stage at a music festival" style="background:linear-gradient(135deg,#5a2a1c,#b0582c 50%,#2a1a14)"><span class="date">15<small>JULY</small></span></div>
    <h5>Foxtrot Lane returns to Riverside Rhythm Festival 2017</h5>
    <p>Foxtrot Lane returns to the Riverside Rhythm Festival this June 30 through July 4. We're so glad we can be a part...[+]</p>
  </article>
  <article class="post" style="left:480px">
    <div class="photo" role="img" aria-label="Festival guest wearing a colourful flower hat" style="background:linear-gradient(135deg,#d46aa8,#e0b24a 50%,#5a8ac8)"><span class="date">15<small>JULY</small></span></div>
    <h5>Foxtrot Lane sponsoring Riverside Rhythm Fest 2016</h5>
    <p>Foxtrot Lane returns to the Riverside Rhythm Festival this June 30 through July 4. We're so glad we can be a part...[+]</p>
  </article>
  <article class="post" style="left:750px">
    <div class="photo" role="img" aria-label="Cleaner vacuuming an office floor" style="background:linear-gradient(135deg,#e8e4da,#8a2a24 50%,#4a8ab4)"><span class="date">15<small>JULY</small></span></div>
    <h5>Foxtrot Lane returns to Riverside Rhythm Festival 2017</h5>
    <p>Foxtrot Lane returns to the Riverside Rhythm Festival this June 30 through July 4. We're so glad we can be a part...[+]</p>
  </article>
  <div class="cta"><span class="btn">View All</span></div>
</section>

<section class="testimonials">
  <h2 class="section-title display"><span><i class="rule l"></i>CLIENT TESTIMONIALS<i class="rule r"></i></span></h2>
  <span class="arrow" style="left:168px;top:120px">&#8249;</span>
  <span class="arrow" style="left:1015px;top:120px">&#8250;</span>
  <div class="quote" style="left:235px">
    <div class="avatar" role="img" aria-label="Client portrait"></div>
    <div><p>"Every room sparkled when they left. Friendly team, fair prices and they arrive right on time. We will book them again soon."</p><div class="name">ADA PENROSE <i>&#9733;&#9733;&#9733;&#9733;</i></div></div>
  </div>
  <div class="quote" style="left:645px">
    <div class="avatar" role="img" aria-label="Client portrait"></div>
    <div><p>"Every room sparkled when they left. Friendly team, fair prices and they arrive right on time. We will book them again soon."</p><div class="name">LEO WHITFORD <i>&#9733;&#9733;&#9733;&#9733;</i></div></div>
  </div>
</section>

<section class="badges paper">
  <span class="cert shield"></span>
  <span class="cert round"></span>
  <span class="cert shield" style="width:70px"></span>
  <span class="cert round"></span>
</section>

<section class="contact">
  <h2 class="section-title display"><span><i class="rule l"></i>CONTACT US<i class="rule r"></i></span></h2>
  <nav class="contact-nav caps"><span class="current">Home</span><span>About Us</span><span>Our Services</span><span>Blog</span><span>Contact Us</span></nav>
  <ul class="contact-info">
    <li><span class="dot-icon"><svg width="12" height="12" viewBox="0 0 12 12"><path d="M6 1a3.5 3.5 0 0 0-3.5 3.5C2.5 7 6 11 6 11s3.5-4 3.5-6.5A3.5 3.5 0 0 0 6 1z" fill="#0b0b0b"/></svg></span><span><b>foxtrotlane</b><br>418 SE Birch St #210, Portland, OR<br>97214</span></li>
    <li><span class="dot-icon"><svg width="12" height="12" viewBox="0 0 12 12"><rect x="1" y="3" width="10" height="7" fill="none" stroke="#0b0b0b" stroke-width="1.5"/></svg></span><span>hello@foxtrotlane.com</span></li>
    <li><span class="dot-icon"><svg width="12" height="12" viewBox="0 0 12 12"><path d="M3 1l2 2-1 2 3 3 2-1 2 2-2 2C5 11 1 7 1 3z" fill="#0b0b0b"/></svg></span><span>T: 503-555-0148</span></li>
    <li><span class="dot-icon"><svg width="12" height="12" viewBox="0 0 12 12"><rect x="2" y="2" width="8" height="8" fill="#0b0b0b"/></svg></span><span>F: +1 503-555-0199</span></li>
  </ul>
  <form class="contact-form">
    <span class="field">Name</span><span class="field">Email</span>
    <span class="field">Phone</span><span class="field">Subject</span>
    <span class="field wide">Message</span>
    <span class="btn">Submit Now</span>
  </form>
</section>

<footer class="site-footer">
  <span>©2018 FOXTROTLANE. ALL RIGHTS RESERVED</span>
  <span class="social"><i></i><i></i><i></i><i></i><i></i></span>
</footer>

</body>
</html>
```